Business card for Chiropractic clinics needs reworked / redesigned

The business card in attachment was designed 10 years ago. It is in need of an update.
We have 2 clinics:
VELDHOVE KLINIEK & VELDHOVE KLINIEK NOORD
Only one address needs to be on the card for doctors that only work in one clinic and two addresses need to be on the card for the doctors that work in both clinics.

Target Market(s)

patients/referrers

Industry/Entity Type

Medical

Contact Information for Business Card

Logo (in full or zoomed-in)
Clinic Name
Doctor name and title
clinic address, website, tel, email

Font styles to use
Sans Serif

Colors

Designer to choose colors to be used in the design.

Requirements
Must have
• Good contrast/readability
• We like modern minimalistic designs
• The Bcard needs to project our very high standard of proficiency/professionalism
Should not have
• Not curly
• Not to much colours

```html
<!DOCTYPE html>
<html lang="nl">
<head>
<meta charset="utf-8">
<title>Veldhove Kliniek – business card</title>
<link href="https://fonts.googleapis.com/css2?family=Quicksand:wght@400;500&display=swap" rel="stylesheet">
<style>
  :root {
    --backdrop: #b4b4b4;
    --card: #141414;
    --card-edge: #1d1d1d;
    --gold: #d9b23a;
    --gold-light: #f3d46a;
    --gold-deep: #a9801c;
    --ink-light: #f4f4f4;
  }
  * { margin: 0; padding: 0; box-sizing: border-box; }
  html, body {
    width: 1200px; height: 1000px; overflow: hidden;
    background: var(--backdrop);
    font-family: "Quicksand", sans-serif;
  }
  .stage {
    position: relative; width: 1200px; height: 1000px;
  }
  .card {
    position: absolute; top: 200px;
    width: 400px; height: 580px;
    background: linear-gradient(160deg, var(--card-edge), var(--card) 60%);
    box-shadow: 0 14px 30px rgba(0,0,0,.35);
    overflow: hidden;
  }
  .card--front { left: 160px; }
  .card--back { left: 640px; }

  .mark-area {
    position: absolute;
    background: linear-gradient(180deg, var(--gold-light), var(--gold) 50%, var(--gold-deep));
    opacity: .85;
    border-radius: 4px;
  }
  .card--front .mark-area--upper { left: 150px; top: 50px; width: 100px; height: 180px; }
  .card--front .mark-area--lower { left: 150px; top: 350px; width: 100px; height: 190px; }
  .card--back .mark-area--spine { left: 0; top: 0; width: 70px; height: 580px; border-radius: 0 4px 4px 0; }

  .doctor {
    position: absolute; left: 0; right: 0; top: 262px;
    text-align: center; color: var(--gold);
  }
  .doctor__name { font-size: 32px; font-weight: 400; letter-spacing: .5px; }
  .doctor__title {
    margin-top: 8px; font-size: 13px; font-weight: 500;
    letter-spacing: 2px; text-transform: uppercase;
  }

  .clinic-name {
    position: absolute; left: 110px; top: 58px;
    color: var(--gold); font-size: 34px; font-weight: 400; letter-spacing: 1px;
  }
  .header-rule {
    position: absolute; left: 110px; right: 30px; top: 108px;
    height: 1px; background: var(--gold);
  }
  .location {
    position: absolute; left: 130px; right: 30px;
  }
  .location--main { top: 128px; }
  .location--north { top: 318px; }
  .location__label {
    color: var(--gold); font-size: 19px; font-weight: 500;
    padding-bottom: 4px; border-bottom: 1px solid var(--gold);
  }
  .location__details {
    list-style: none; margin-top: 8px;
    color: var(--ink-light); font-size: 21px; line-height: 31px; font-weight: 500;
  }
</style>
</head>
<body>
<main class="stage">
  <section class="card card--front" aria-label="Card front">
    <div class="mark-area mark-area--upper" role="img" aria-label="Clinic logo mark, upper part"></div>
    <div class="doctor">
      <p class="doctor__name">Maarten Verlinde</p>
      <p class="doctor__title">Chiropractor</p>
    </div>
    <div class="mark-area mark-area--lower" role="img" aria-label="Clinic logo mark, lower part"></div>
  </section>

  <section class="card card--back" aria-label="Card back">
    <div class="mark-area mark-area--spine" role="img" aria-label="Clinic logo mark as side decoration"></div>
    <h1 class="clinic-name">VELDHOVE</h1>
    <div class="header-rule"></div>

    <div class="location location--main">
      <p class="location__label">kliniek</p>
      <ul class="location__details">
        <li>Lindendreef 48</li>
        <li>09 000 41 27</li>
        <li>veldhovekliniek.be</li>
      </ul>
    </div>

    <div class="location location--north">
      <p class="location__label">kliniek noord</p>
      <ul class="location__details">
        <li>Kerkwegel 17</li>
        <li>09 000 86 52</li>
        <li>veldhovenoord.be</li>
      </ul>
    </div>
  </section>
</main>
</body>
</html>
```